Vallée douce coffee - Label design

Watchout: Keep in mind while you submit it needs to be a LABEL (that will be sticked on brown kraft 250 g side gusset coffee pouches). No custom pack for time being (need more scale to custom print pack).

Looking for a label design for my new Beau Matin collection of freshly roasted, single origin specialty coffee. Brand name is Vallée Douce (it means red earth and alludes to the soil coffee grows on at high altitude in Africa. It also alludes to the red color of the coffee fruit). Brand selling line is "Pure Origin Coffee". Label to go as stickers on 250 g side gusset coffee pouches in Kraft brown paper (will print labels and stick on packs, packs are 80 mm wide and 260 mm long). This is a relatively complex project comprising the "vallée douce" brand logo (funded separately, winner will have the job), the "Beau Matin" collection visual identity, iconic assets for brand and collection recognition across lineup, educational visual icons, text placeholders. It needs to combine hard point visual elements and soft points (text placeholder) which I can easily edit on need basis (text needs to be "outlines" for easy editing after submission). Winner of label submission gets to design brand logo. I will ultimately need 3 different labels for our Beau Matin collection, one for each continent our coffee comes from (Africa, Asia, Latin America). This pitch should focus on the Africa one only. Winner will then have opportunity to design the other ones in consistent way.

BRIEF:
We roast single origin, high quality specialty coffee from high altitude estates in Africa (volcanic slopes in Congo and Burundi, Highlands in Ethiopia and Kenya) Design need to induce the premiumness of the proposition (this is a collection called "Beau Matin"), as well the the unique geographical origins of our coffee (without being too specific as we want to use same label for all our African origins) -oversized shape of continent in background + some visuals conveying the African roots could work well. It needs to create a mental Journey "back to the origins" - of mankind, of unique terroirs creating the best coffee, of our unspoilt roots. So the Journey themes is critical (to be expressed by the telegram type of font, by the way Africa is brought to life,etc.). At the same time keep in mind label space is limited (label stickers go on 250 g coffee pouches made in kraft brown paper) and we want to have a pure design, which leaves room to the text placeholder (see below) and is easily recognizable and reapplicable across the SKUs (we will add Asia and Latin America packs once we lock Africa). As such we need to strike right balance between visual differentiation by origin (Africa, Asia, Latin America) and common iconic assets for brand recognition and lineup harmonization (same font, same way the continent is brought to life, same structure of the label, differentiation by color background,etc.).

We need placeholder for text that will specify exact name of estate, county of origin, coffee type, roasting level and tasting notes. Here I will allow myself some creative direction: it should be in the format of a vintage luggage tag (see attached examples) where we can edit content in Telegram font (our coffee sourcing changes often). We will need to assess if the tag remains standard across collection, or whether we are able to give it a visual twist for each origin (Africa, Asia, Latin America). That would be nicer (see Moonpeak "Ledgers" example), but priority of the text placeholder is clarity of information above anything else.

Last nice to have (if it time allows) we need educational visual icons (ideally as separate small round labels we can stick on the pack above the main label) for recommended brewing method (filter, espresso, italian moka, french press).

Reason: Still looking for the design in line with brief. Will send feedback to the top 3 routes today.

Target Market(s)

Switzerland

Industry/Entity Type

Coffee Shop

Logo Text

Vallée douce -Pure Origin Coffee

Font styles to use
Other font styles liked:
• TELEGRAM type of font to induce geographical journey, single origin,.. For the "luggage tag" placeholder

Requirements
Must have
• - Brand name: Vallée Douce. Brand selling line: Pure Origin Coffee. Brand Logo: winner of label submission gets to design brand logo
• - Collection name: BEAU MATIN (written, I can see well as a vertical block). name of SKU: AFRICA (visualized a must, written tbc).
• - Text place holder (vintage luggage tag in telegram font) : we will show there name of estate, country of origin, tasting notes. I could see nicely a baggage tag format, where we fill in the details in telegram type of font.
• - 100% single origin Arabica (at the bottom)
• - 250 g (at the bottom)
• Technical Specs:
• A. Artwork must be supplied in either Adobe illustrator or Adobe Photoshop files or Coral Draw files
• B. Create all text in artwork in ‘ outlines ’
• C. The resolution of photographic image files must be no less than 350 dpi
• D. Never flatten the file as we require all layers
• E. All Photoshop image files should be linked and attached. Never flatten the layers and do not change the directory
• F. Create the images with CMYK colour mode ( RGB colour mode is not for printing)
• G. If you are going to use a spot colour please reference the Pantone ( PMS #)
• H. Designate all ‘Transparent’ areas in the artwork with a custom Pantone colour as well as designating the layer’s name as ‘ Transparent’. Please indicate specifically which pantone colour is designated for the ‘transparent’ area.
• I. Reduce any barcodes to 85% as a minimum scale
Nice to have
• - educational simple visual icons on recommended brewing method (filer, italian moka, french press or espresso) as additional small stickers to stick above main label

```html
<!DOCTYPE html>
<html lang="en">
<head>
<meta charset="utf-8">
<title>Vallée Douce – Beau Matin Africa label</title>
<link href="https://fonts.googleapis.com/css2?family=Alfa+Slab+One&family=Bebas+Neue&family=Courier+Prime:wght@400;700&family=Great+Vibes&family=Josefin+Sans:wght@400&display=swap" rel="stylesheet">
<style>
  :root {
    --kraft: #c8ad8c;
    --ink: #1f1c1a;
    --label-white: #ffffff;
    --origin-blue: #1238e0;
    --strip-blue: #3d63d6;
    --map-tint: #6f8ef2;
    --rule-grey: #6b6b6b;
  }
  * { margin: 0; padding: 0; box-sizing: border-box; }
  html, body { width: 1200px; height: 900px; overflow: hidden; }
  body {
    background: var(--kraft);
    position: relative;
    font-family: "Courier Prime", "Courier New", monospace;
    color: var(--ink);
  }

  .brand-block {
    position: absolute;
    top: 120px; left: 0; width: 1200px;
    display: flex; flex-direction: column; align-items: center;
  }
  .brand-dot {
    width: 130px; height: 130px;
    border-radius: 50%;
    background: var(--ink);
    margin-bottom: 44px;
  }
  .brand-name {
    font-family: "Alfa Slab One", Georgia, serif;
    font-size: 58px;
    letter-spacing: 4px;
    line-height: 1;
  }
  .brand-descriptor {
    margin-top: 14px;
    font-family: "Josefin Sans", Arial, sans-serif;
    font-size: 30px;
    letter-spacing: 4px;
    line-height: 1;
  }

  .origin-label {
    position: absolute;
    top: 530px; left: 220px;
    width: 760px; height: 220px;
    background: var(--label-white);
    display: flex;
  }
  .origin-label::before,
  .collection-strip::after {
    content: "";
    position: absolute;
    top: 0;
    width: 14px; height: 100%;
    background: radial-gradient(circle at 7px 10px, var(--kraft) 5px, transparent 5.5px) 0 0 / 14px 20px repeat-y;
  }
  .origin-label::before { left: -7px; }

  .origin-map {
    margin: 30px 0 0 26px;
    width: 200px; height: 160px;
    background: var(--origin-blue);
    position: relative;
    flex-shrink: 0;
  }
  .origin-map__shape {
    position: absolute;
    inset: 12px 36px;
    background: radial-gradient(ellipse at 45% 40%, var(--map-tint) 0%, var(--origin-blue) 78%);
  }
  .origin-map__name {
    position: absolute;
    left: 18px; bottom: 22px;
    font-family: "Great Vibes", cursive;
    font-size: 42px;
    line-height: 1;
    color: var(--label-white);
  }

  .tag-details {
    flex: 1;
    padding: 24px 14px 0 20px;
  }
  .tag-row {
    display: flex;
    align-items: center;
    padding-bottom: 8px;
  }
  .tag-row--top { border-bottom: 2px solid var(--rule-grey); }
  .tag-row--mid { padding-top: 10px; }
  .tag-divider {
    width: 2px; height: 30px;
    background: var(--ink);
    margin: 0 12px;
  }
  .selling-line {
    font-family: "Bebas Neue", Impact, sans-serif;
    font-size: 36px;
    line-height: 1.1;
  }
  .net-weight {
    font-family: Georgia, "Times New Roman", serif;
    font-size: 19px;
  }
  .roast-caption {
    font-family: "Bebas Neue", Impact, sans-serif;
    font-size: 26px;
    color: var(--origin-blue);
    margin-right: 10px;
  }
  .roast-date { font-size: 20px; }
  .certification {
    font-family: "Bebas Neue", Impact, sans-serif;
    font-size: 36px;
    line-height: 1.1;
  }
  .craft-band {
    margin-top: 8px;
    background: var(--origin-blue);
    color: var(--label-white);
    font-size: 19px;
    letter-spacing: 1.5px;
    text-align: center;
    padding: 8px 0;
  }

  .collection-strip {
    width: 66px;
    background: var(--strip-blue);
    position: relative;
    flex-shrink: 0;
    display: flex; align-items: center; justify-content: center;
  }
  .collection-strip::after { right: -7px; }
  .collection-name {
    transform: rotate(-90deg);
    white-space: nowrap;
    font-family: "Bebas Neue", Impact, sans-serif;
    font-size: 40px;
    letter-spacing: 2px;
    color: var(--label-white);
  }
</style>
</head>
<body>
  <header class="brand-block">
    <span class="brand-dot"></span>
    <div class="brand-name">VALLÉE DOUCE</div>
    <div class="brand-descriptor">COFFEE ROASTERS</div>
  </header>

  <section class="origin-label">
    <div class="origin-map">
      <div class="origin-map__shape" role="img" aria-label="Map of the African continent over a faint globe grid"></div>
      <span class="origin-map__name">Africa</span>
    </div>

    <div class="tag-details">
      <div class="tag-row tag-row--top">
        <span class="selling-line">PURE ORIGIN COFFEE</span>
        <span class="tag-divider"></span>
        <span class="net-weight">12 OZ / 250 G</span>
      </div>
      <div class="tag-row tag-row--mid">
        <span class="roast-caption">ROASTED ON:</span>
        <span class="roast-date">12/04/2015</span>
        <span class="tag-divider"></span>
        <span class="certification">ORGANIC</span>
      </div>
      <div class="craft-band">FRESH ROASTED • HANDY CRAFTED</div>
    </div>

    <div class="collection-strip">
      <span class="collection-name">BEAU MATIN</span>
    </div>
  </section>
</body>
</html>
```